Financial Planning Pyramid Graphic

I need a graphic of a pyramid including 3 levels.

I've attached a copy of the article to be published with the graphic.

Also attached company logos if it makes sense to use.

See www.NovalisCapitalAdvisors.com for a general reference.

Target Market(s)

small and medium size business owners who intend to eventually sell their business. primarily servicing the construction, real estate, and technology industries.

Industry/Entity Type

Financial Planning

Font styles to use
Sans Serif

Requirements
Must have
• Primary branding hex color #009b81

Three levels of the pyramid:
3. Top: Wealth Distribution
2. Middle: Growing Wealth
1. Base: Protection (Risk Management)

It should somehow show how "Tax Planning" permeates all 3 layers.
Nice to have
• The attached article includes details about what the graphic should represent and more details that may be included.

```html
<!DOCTYPE html>
<html lang="en">
<head>
<meta charset="utf-8">
<title>Financial Planning Pyramid</title>
<link rel="stylesheet" href="https://fonts.googleapis.com/css2?family=Montserrat:wght@700&family=Questrial&display=swap">
<style>
  :root {
    --teal-light: #00b9a3;
    --teal-mid: #00a88f;
    --teal-brand: #009b81;
    --teal-deep: #008f75;
    --shadow-dark: #1c1c1c;
    --shadow-mid: #333333;
    --tax-orange: #f9b03a;
    --text-white: #ffffff;
    --page: #ffffff;
  }
  html, body {
    margin: 0;
    padding: 0;
    width: 1200px;
    height: 1200px;
    overflow: hidden;
    background: var(--page);
  }
  .canvas {
    display: block;
    width: 1200px;
    height: 1200px;
  }
  .level-title {
    font-family: "Montserrat", "Century Gothic", sans-serif;
    font-weight: 700;
    font-size: 33px;
    fill: var(--text-white);
    text-anchor: middle;
  }
  .level-items {
    font-family: "Questrial", "Century Gothic", sans-serif;
    font-size: 21px;
    fill: var(--text-white);
    text-anchor: middle;
  }
  .tax-label {
    font-family: "Montserrat", "Century Gothic", sans-serif;
    font-weight: 700;
    font-size: 19px;
    letter-spacing: 3px;
    fill: var(--text-white);
    text-anchor: middle;
  }
</style>
</head>
<body>
<svg class="canvas" viewBox="0 0 1200 1200" xmlns="http://www.w3.org/2000/svg">
  <defs>
    <linearGradient id="tealFace" x1="0" y1="0" x2="1" y2="1">
      <stop offset="0" stop-color="var(--teal-light)"/>
      <stop offset="0.55" stop-color="var(--teal-mid)"/>
      <stop offset="1" stop-color="var(--teal-deep)"/>
    </linearGradient>
    <linearGradient id="reflection" x1="0" y1="0" x2="0" y2="1">
      <stop offset="0" stop-color="#b4e2d8"/>
      <stop offset="1" stop-color="#ffffff"/>
    </linearGradient>
    <radialGradient id="groundShadow" cx="0.5" cy="0.5" r="0.5">
      <stop offset="0" stop-color="#000" stop-opacity="0.35"/>
      <stop offset="1" stop-color="#000" stop-opacity="0"/>
    </radialGradient>
  </defs>

  <polygon class="pyramid-reflection" points="147,1031 1133,1031 1055,1190 225,1190" fill="url(#reflection)"/>
  <ellipse class="ground-shadow" cx="640" cy="1031" rx="560" ry="9" fill="url(#groundShadow)"/>

  <polygon class="level level-top" points="640,45 779,320 536,320" fill="url(#tealFace)"/>
  <polygon class="level-gap" points="550,320 779,320 724,356 519,356" fill="var(--shadow-mid)"/>
  <polygon class="level-gap-edge" points="550,320 779,320 527,343" fill="var(--shadow-dark)"/>

  <polygon class="level level-middle" points="519,356 795,356 950,663 366,663" fill="url(#tealFace)"/>
  <polygon class="level-gap" points="456,663 950,663 829,706 348,706" fill="var(--shadow-mid)"/>
  <polygon class="level-gap-edge" points="456,663 950,663 946,666 356,688" fill="var(--shadow-dark)"/>

  <polygon class="level level-base" points="348,706 971,706 1133,1031 147,1031" fill="url(#tealFace)"/>

  <text class="level-title" x="654" y="275" textLength="104" lengthAdjust="spacingAndGlyphs">WEALTH</text>
  <text class="level-title" x="654" y="307" textLength="182" lengthAdjust="spacingAndGlyphs">DISTRIBUTION</text>

  <text class="level-title" x="654" y="491" textLength="145" lengthAdjust="spacingAndGlyphs">GROWING</text>
  <text class="level-title" x="654" y="524" textLength="104" lengthAdjust="spacingAndGlyphs">WEALTH</text>
  <text class="level-items" x="656" y="573" textLength="429" lengthAdjust="spacingAndGlyphs">•&#160;Investment Planning &#160;•&#160;Retirement Planning</text>
  <text class="level-items" x="656" y="599" textLength="201" lengthAdjust="spacingAndGlyphs">•&#160;Education Planning</text>

  <text class="level-title" x="654" y="858" textLength="175" lengthAdjust="spacingAndGlyphs">PROTECTION</text>
  <text class="level-title" x="655" y="892" textLength="284" lengthAdjust="spacingAndGlyphs">(RISK MANAGEMENT)</text>
  <text class="level-items" x="656" y="934" textLength="601" lengthAdjust="spacingAndGlyphs">•&#160;Emergency Savings &#160;•&#160;Insurance Coverages &#160;•&#160;Executed Will</text>

  <g class="tax-arrow" fill="var(--tax-orange)">
    <polygon points="552,217 582,230 318,765 290,750"/>
    <polygon points="584,178 595,230 544,212"/>
    <polygon points="281,797 276,744 327,770"/>
  </g>
  <text class="tax-label" transform="translate(422,515) rotate(-63.9)">TAX PLANNING</text>
</svg>
</body>
</html>
```